Personal Business Card

Looking for a clean and modern personal business card. Basically I need something catchy to give to potential clients and people I meet. I do a lot of freelancing (from DJ'ing to wedding videography, but its mostly on the event side of things) so it's more-so about selling myself rather than identifying with a company. I'm starting to meet more people that I want to work with after meeting them so I'm revamping my business cards.

I'm looking for a clean and modern design- I know that's really vague but I'm fine with anything ranging from a symbol to just a fancy version of my name.

Details I need on the front:
Dennis Kowal
dennis@denniskowal-mail.net
(555) 807-2291

On the back I'd like to have something simple like "Nice to have met you today" or "Great meeting you".

UPDATE 9/27 Noon: My apologies for not putting it up before- I'm definitely looking for full color. Doesn't have to be a rainbow but I am looking for the least amount of blank white as possible.

UPDATE 10/1: Really impressed with what I've been getting so far and I'm working on giving everyone feedback- if your design is still up then you're still in the run. Looking for something more unique and modern so please do not post something that looks like a template from Cardloom!

Target Market(s)

Mainly to give to people aged 18-35. Most of my encounters will be casual so the card should have a "young" feeling to it. I rarely do anything in the corporate world so it doesn't have to be boring. It should give the impression that I'm the one they should go to if they need what I do (again it changes every weekend so I'll probably say the "what I do" part.

Industry/Entity Type

Wedding

Requirements
Must have
• Basically the contact information listed above
Nice to have
• I really like the colors Blue, Silver, and Purple. They don't have to necessarily all be there though. I do like the look of polished metal if that makes sense.
Should not have
• A template that resembles card-loom. I'm in a point in my life where I'm working a lot of different markets/areas so the card does not need to have an address or address placeholder.

```html
<!DOCTYPE html>
<html lang="en">
<head>
<meta charset="utf-8">
<title>Dennis Kowal – Business Card</title>
<link rel="stylesheet" href="https://fonts.googleapis.com/css2?family=Arimo:ital,wght@1,700&display=swap">
<style>
  :root {
    --backdrop: #a9a9a9;
    --card-white: #ffffff;
    --navy: #0b0b7d;
    --divider-grey: #9c9c9c;
    --icon-blue: #3a7fd6;
    --text-white: #ffffff;
  }
  * { box-sizing: border-box; margin: 0; padding: 0; }
  html, body {
    width: 1200px;
    height: 900px;
    overflow: hidden;
    background: var(--backdrop);
    font-family: "Arimo", Arial, sans-serif;
  }
  .canvas {
    width: 1200px;
    height: 900px;
    display: flex;
    flex-direction: column;
    align-items: center;
    justify-content: center;
    gap: 60px;
  }
  .card {
    position: relative;
    width: 640px;
    height: 366px;
    background: var(--card-white);
    box-shadow: 0 4px 10px rgba(0,0,0,0.25);
    overflow: hidden;
  }
  .card__band {
    position: absolute;
    left: 0;
    right: 0;
    bottom: 0;
    background: var(--navy);
    border-top: 10px solid var(--divider-grey);
  }
  .card--front .card__band { height: 48%; }
  .card--back .card__band { height: 40%; }

  .card__name,
  .card__greeting {
    position: absolute;
    left: 40px;
    color: var(--navy);
    font-weight: 700;
    font-style: italic;
    white-space: nowrap;
  }
  .card__name {
    bottom: 56%;
    font-size: 50px;
  }
  .card__greeting {
    bottom: 45%;
    font-size: 40px;
  }

  .contact {
    position: absolute;
    right: 30px;
    top: 58%;
    list-style: none;
    display: flex;
    flex-direction: column;
    gap: 8px;
  }
  .contact__item {
    display: flex;
    align-items: center;
    gap: 10px;
    color: var(--text-white);
    font-weight: 700;
    font-style: italic;
    font-size: 20px;
  }
  .contact__item--email { font-size: 16px; }
  .contact__icon { width: 26px; height: 26px; flex: none; }
</style>
</head>
<body>
<main class="canvas">
  <section class="card card--front" aria-label="Card front">
    <h1 class="card__name">DJ Dennis Kowal</h1>
    <div class="card__band"></div>
    <ul class="contact">
      <li class="contact__item">
        <svg class="contact__icon" viewBox="0 0 26 26" aria-hidden="true">
          <circle cx="13" cy="13" r="12" fill="var(--icon-blue)" stroke="#fff" stroke-width="1"/>
          <path d="M9 7 l3 0 l1 4 l-2 1.5 q1.5 3 4 4 l1.5 -2 l4 1 l0 3 q-9 1 -11.5 -11.5z" fill="#fff"/>
        </svg>
        <span>(555) 807-2291</span>
      </li>
      <li class="contact__item contact__item--email">
        <svg class="contact__icon" viewBox="0 0 26 26" aria-hidden="true">
          <circle cx="13" cy="13" r="12" fill="var(--icon-blue)" stroke="#fff" stroke-width="1"/>
          <rect x="6.5" y="8.5" width="13" height="9" fill="#fff"/>
          <path d="M6.5 8.5 l6.5 5 l6.5 -5" fill="none" stroke="var(--icon-blue)" stroke-width="1.2"/>
        </svg>
        <span>dennis@denniskowal-mail.net</span>
      </li>
    </ul>
  </section>

  <section class="card card--back" aria-label="Card back">
    <p class="card__greeting">Nice to have met you today.</p>
    <div class="card__band"></div>
  </section>
</main>
</body>
</html>
```